Mortgage Loan officer needs clean/modern business card design

Looking for a clean, modern 2-sided business card design. We like the earth tones used in our logo and website http://vukarhome-lending.example . Would also like to incorporate: 1) Something special to make our card stand out - a pop of color or embossed logo, for instance and 2) please include "Mortgage Loans" "Reverse Mortgages" "Private Money Loans" on back of card with the logo.

Front: Needs to include agent/company license info - see website. Agent name: Niall Hargrove

Here are fonts and colors used for our logo:
Font: Avenir Next
Colors:
#2c3539 - Dark Gray
#576870 - Light Gray
#ffffff - Background White

Target Market(s)

Prospects and current clients. Will also be distributing to people in professional network (attorneys and CPAs)

Industry/Entity Type

Business

Contact Information for Business Card

Include agent name, contact info, website on front, licensing info for agent an company. Logo and services offered on back

Font styles to use
Other font styles liked:
• Avenir Next

Requirements
Must have
• See project description
Should not have
• Nothing cheesy

```html
<!DOCTYPE html>
<html lang="en">
<head>
<meta charset="utf-8">
<title>Vukar Home Lending – Business Card</title>
<link rel="stylesheet" href="https://fonts.googleapis.com/css2?family=Mulish:wght@400;600;700;800&display=swap">
<style>
  :root {
    --dark-gray: #2c3539;
    --light-gray: #576870;
    --white: #ffffff;
    --backdrop: #3a3d40;
    --outline: #8a969b;
  }
  * { margin: 0; padding: 0; box-sizing: border-box; }
  html, body {
    width: 1200px; height: 864px; overflow: hidden;
    background: var(--backdrop);
    font-family: "Mulish", sans-serif;
  }
  .canvas { position: relative; width: 1200px; height: 864px; }

  .card {
    position: absolute; left: 320px; width: 560px; height: 320px;
    background: var(--white); overflow: hidden;
    box-shadow: 0 10px 26px rgba(0,0,0,0.35);
  }

  /* Back of card */
  .card-back { top: 64px; background: var(--dark-gray); }
  .card-back .white-band {
    position: absolute; left: 0; right: 0; top: 58px; height: 132px;
    background: var(--white);
  }
  .card-back .seal {
    position: absolute; left: 50%; top: 50px; transform: translateX(-50%);
    width: 148px; height: 148px; border-radius: 50%;
    background: var(--white); border: 9px solid var(--dark-gray);
    display: flex; align-items: center; justify-content: center; text-align: center;
  }
  .brand-name {
    color: var(--light-gray); font-weight: 600; font-size: 16px; line-height: 1.2;
  }
  .services {
    position: absolute; left: 0; right: 0; top: 222px;
    text-align: center; color: var(--white);
    font-weight: 700; font-size: 15px; letter-spacing: 0.6px; line-height: 1.35;
    text-transform: uppercase;
  }
  .services .divider { padding: 0 8px; font-weight: 400; }

  /* Front of card */
  .card-front { top: 480px; }
  .card-front .side-band {
    position: absolute; left: 34px; top: 0; width: 150px; height: 100%;
    background: var(--dark-gray);
  }
  .card-front .seal {
    position: absolute; left: 24px; top: 24px;
    width: 154px; height: 154px; border-radius: 50%;
    background: var(--white); border: 1.5px solid var(--outline);
    display: flex; align-items: center; justify-content: center; text-align: center;
  }
  .agent { position: absolute; left: 222px; top: 22px; }
  .agent-name { color: var(--dark-gray); font-weight: 800; font-size: 20px; letter-spacing: 0.2px; }
  .agent-title { color: var(--light-gray); font-weight: 400; font-size: 14px; margin-top: 1px; }

  .address {
    position: absolute; left: 214px; top: 172px;
    color: var(--light-gray); font-size: 14px; line-height: 1.25;
  }
  .contacts { position: absolute; left: 212px; top: 218px; list-style: none; }
  .contacts li {
    display: flex; align-items: center; gap: 10px;
    color: var(--light-gray); font-size: 14px; height: 20px;
  }
  .contacts svg { width: 11px; height: 11px; fill: var(--dark-gray); flex: none; }
</style>
</head>
<body>
<main class="canvas">

  <section class="card card-back" aria-label="Back of business card">
    <div class="white-band"></div>
    <div class="seal"><span class="brand-name">Vukar Home<br>Lending</span></div>
    <p class="services">
      Mortgage Loans<span class="divider">|</span>Reverse Mortgages<br>Private Money Loans
    </p>
  </section>

  <section class="card card-front" aria-label="Front of business card">
    <div class="side-band"></div>
    <div class="seal"><span class="brand-name">Vukar Home<br>Lending</span></div>

    <div class="agent">
      <h1 class="agent-name">Jonathan Smith</h1>
      <p class="agent-title">Managing Director</p>
    </div>

    <p class="address">12345, Address Goes Here<br>Country Name, 123456</p>

    <ul class="contacts">
      <li>
        <svg viewBox="0 0 12 12" aria-hidden="true"><path d="M2.4 0.6l1.9 1.9-1 1.4c.7 1.6 2 2.9 3.6 3.6l1.4-1 1.9 1.9-1.3 2C5 10.2 1.6 6.8 0.4 1.9z"/></svg>
        (044)-456-7890
      </li>
      <li>
        <svg viewBox="0 0 12 12" aria-hidden="true"><path d="M3 0h6v12H3zM4 1.5v8h4v-8z"/></svg>
        123-456-7890
      </li>
      <li>
        <svg viewBox="0 0 12 12" aria-hidden="true"><path d="M0 2h12v8H0zM1 3l5 3.6L11 3z" fill-rule="evenodd"/></svg>
        info@youremail.com
      </li>
      <li>
        <svg viewBox="0 0 12 12" aria-hidden="true"><circle cx="6" cy="6" r="5.5"/><path d="M1 6h10M6 .5c2 2 2 9 0 11M6 .5c-2 2-2 9 0 11" stroke="#fff" stroke-width="0.8" fill="none"/></svg>
        www.website.com
      </li>
    </ul>
  </section>

</main>
</body>
</html>
```